Dental Business Card Design w/logo

Classic, elegant w/a touch of contemporary
Upscale dental facility located in Modesto CA
Specializing in restorative & general dentistry
Providing exceptional customer service to the community
Updates

I prefer script and not bold writing
If you can use the phone; fax and email icons instead of spelling them out, it would be great
No bold colors
Classy and elegant
In the back of the card I would like to see something like this
Your Next Appointment:
Mon     Tue    Wed    Thur (a box next to each of them for marking)
Date:_______________ at_____________ AM    PM  (a box next to them for marking)

Thank you

Target Market(s)

Well established professional

Industry/Entity Type

Dental

Contact Information for Business Card

Velorine Tamsuki DMD
4176 Larchmont Rd
Suite D7
Modesto, CA 95368

Office: 209-731-5092
Fax: 209-731-8247
Email: tamsukidmd@brivelmail.test

Requirements
Must have
• Unique classic logo
An easily repeatable design that can be used on letterhead and envelopes
Nice to have
• My initials incorporated into unique design
Should not have
• No cartoons or cheesy themes. This is a practice for the well established and professional individual.

```html
<!DOCTYPE html>
<html lang="en">
<head>
<meta charset="utf-8">
<title>Velorine Tamsuki Dental — Business Card</title>
<link rel="stylesheet" href="https://fonts.googleapis.com/css2?family=Roboto:wght@300&display=swap">
<style>
  :root {
    --backdrop: #e8ede2;
    --card-top: #6ccbdc;
    --card-bottom: #00b4ca;
    --ink: #ffffff;
    --shadow: rgba(40, 60, 50, 0.22);
  }
  html, body {
    margin: 0;
    padding: 0;
    width: 1200px;
    height: 901px;
    overflow: hidden;
    background: var(--backdrop);
  }
  .stage {
    position: relative;
    width: 1200px;
    height: 901px;
  }
  .card {
    position: absolute;
    left: 250px;
    top: 250px;
    width: 700px;
    height: 400px;
    background: linear-gradient(to bottom, var(--card-top), var(--card-bottom));
    box-shadow: 0 8px 24px var(--shadow);
    color: var(--ink);
    font-family: "Roboto", "Helvetica Neue", Arial, sans-serif;
    font-weight: 300;
  }
  .wordmark {
    position: absolute;
    left: 0;
    right: 0;
    top: 118px;
    text-align: center;
  }
  .wordmark__name {
    margin: 0;
    font-size: 40px;
    letter-spacing: 0.5px;
    line-height: 1.1;
  }
  .wordmark__tag {
    margin: 10px 0 0;
    font-size: 17px;
    letter-spacing: 5px;
    line-height: 1;
  }
  .address {
    position: absolute;
    right: 34px;
    top: 238px;
    margin: 0;
    text-align: right;
    font-style: normal;
    font-size: 17px;
    line-height: 27px;
  }
  .contact {
    position: absolute;
    left: 34px;
    bottom: 28px;
    margin: 0;
    font-style: normal;
    font-size: 17px;
    line-height: 27px;
  }
  .contact__credential {
    font-size: 11px;
    letter-spacing: 0.5px;
  }
  .contact span.line,
  .address span.line {
    display: block;
  }
</style>
</head>
<body>
  <main class="stage">
    <section class="card" aria-label="Business card front">
      <div class="wordmark">
        <p class="wordmark__name">Velorine Tamsuki</p>
        <p class="wordmark__tag">DENTAL</p>
      </div>

      <address class="address">
        <span class="line">4176 Larchmont Rd</span>
        <span class="line">Suite D7 Modesto CA 95368</span>
        <span class="line">tamsukidmd@brivelmail.test</span>
      </address>

      <address class="contact">
        <span class="line">Velorine Tamsuki <span class="contact__credential">DMD</span></span>
        <span class="line">t. 209-731-5092</span>
        <span class="line">f. 209-731-8247</span>
      </address>
    </section>
  </main>
</body>
</html>
```